Business card for a boutique travel agency VELIRANDE

we need a business card design - double sided. We would like to have a very elegant, sophisticated but modern design. we are travel consultants and our business focus is Europe, mainly the city of Paris. We would like to receive designs in white and silver, black color but if you are confident that we should pick up a color to make it different and more beautful...go ahead! We are going to give business cards to our clients and business partners. It is important to be perceived as elegant, modern and trustful. Please check jpg references.

Target Market(s)

Velirande primary clients are individuals, couples and affinity groups of high-net-worth who travel for leisure at least once per year. Seeking the ultimate travel experience, the target clients demand the finest quality activities and accommodations accompanied by a superior level of service.

Industry/Entity Type

Travel Industry

Contact Information for Business Card

Liliana Quesada
- liliana@velirande-mail.example
- +55 11 98437.5216
- velirande-mail.example
- unique travel experiences (we would like to see this signature printed as a detail)

Font styles to use
Sans Serif

Colors

Designer to choose colors to be used in the design.

Requirements
Must have
• the Velirande logo that I have attached
Nice to have
• we would like to have some nice detail, something different that shows that we care about,... we are detail oriented.
Should not have
• decorative fonts

```html
<!DOCTYPE html>
<html lang="en">
<head>
<meta charset="utf-8">
<title>Velirande — Business Card</title>
<link rel="stylesheet" href="https://fonts.googleapis.com/css2?family=Josefin+Sans:wght@300&family=Open+Sans:wght@400&display=swap">
<style>
  :root {
    --backdrop: #e6e3df;
    --card: #1b1b1b;
    --emboss: #545454;
    --tagline: #6e6e6e;
    --ink-light: #f2f2f2;
    --ink-soft: #e4e4e4;
  }
  * { margin: 0; padding: 0; box-sizing: border-box; }
  html, body {
    width: 1200px; height: 1000px; overflow: hidden;
    background: var(--backdrop);
  }
  .canvas { position: relative; width: 1200px; height: 1000px; }
  .card {
    position: absolute; left: 266px; width: 666px; height: 397px;
    background: var(--card);
  }
  .card--front { top: 74px; }
  .card--back { top: 533px; }

  .wordmark {
    font-family: "Josefin Sans", sans-serif;
    font-weight: 300;
    text-transform: uppercase;
    white-space: nowrap;
    position: absolute;
  }
  .card--front .wordmark {
    left: 0; right: 0; top: 176px;
    text-align: center;
    font-size: 44px; letter-spacing: 0.3em; text-indent: 0.3em;
    color: var(--emboss);
  }
  .tagline {
    position: absolute; left: 0; right: 0; top: 349px;
    text-align: center;
    font-family: "Open Sans", sans-serif; font-size: 16px;
    color: var(--tagline);
  }
  .card--back .wordmark {
    left: 31px; top: 90px;
    font-size: 30px; letter-spacing: 0.3em;
    color: var(--ink-light);
  }
  .holder {
    position: absolute; left: 33px; top: 202px;
    font-family: "Open Sans", sans-serif; font-size: 17px;
    text-transform: uppercase; color: var(--ink-light);
  }
  .contact {
    position: absolute; left: 32px; top: 245px;
    list-style: none;
    font-family: "Open Sans", sans-serif; font-size: 15px;
    line-height: 24.5px; color: var(--ink-soft);
  }
  .contact .address { margin-top: 7px; }
</style>
</head>
<body>
  <main class="canvas">
    <section class="card card--front" aria-label="Card front">
      <div class="wordmark">Velirande</div>
      <p class="tagline">Unique Travel Experiences</p>
    </section>

    <section class="card card--back" aria-label="Card back">
      <div class="wordmark">Velirande</div>
      <p class="holder">Liliana Quesada</p>
      <ul class="contact">
        <li>+55 11 98437.5216</li>
        <li>liliana@velirande-mail.example</li>
        <li>www.velirande-mail.example</li>
        <li class="address">Ashcombe, Fernbury, TX14 4QZ</li>
      </ul>
    </section>
  </main>
</body>
</html>
```